Need business cards for our e-assessment business

We need professional looking business cards for our e-assessment business based in Europe. Our company is called Velmora.

You can just use sample name and addresses.

The colours we use are:

#70abe4 (blue)
#FF6600 (orange)

The back side should say: E-assessment made easy

This is the print-shop we are using. Please look at the link for info about formats: http://nl.pribbly-print.com/help/faq/using-my-own-artwork.html

Target Market(s)

Target market is education and large corporations

Industry/Entity Type

Business

```html
<!DOCTYPE html>
<html lang="en">
<head>
<meta charset="utf-8">
<title>Velmora business cards</title>
<link rel="stylesheet" href="https://fonts.googleapis.com/css2?family=Jost:wght@500;600&family=Open+Sans:wght@400&family=Questrial&display=swap">
<style>
  :root {
    --bg: #ebedec;
    --blue: #70abe4;
    --orange: #f07820;
    --ink: #3a3a3a;
    --ink-soft: #555555;
    --white: #ffffff;
  }
  * { margin: 0; padding: 0; box-sizing: border-box; }
  html, body { width: 944px; height: 1200px; overflow: hidden; background: var(--bg); }
  .canvas { position: relative; width: 944px; height: 1200px; }

  .card {
    position: absolute;
    width: 645px;
    height: 431px;
    box-shadow: -6px 8px 14px rgba(0,0,0,0.28);
    overflow: hidden;
  }
  .card--front {
    left: 144px; top: 122px;
    background: linear-gradient(90deg,
      var(--blue) 0%, #a9cbee 10%, var(--white) 24%,
      var(--white) 61%, #fbe2cf 70%, #f5a96c 88%, var(--orange) 100%);
  }
  .card--back {
    left: 140px; top: 643px;
    background: linear-gradient(90deg,
      var(--orange) 0%, #f5a96c 12%, #fbe2cf 26%, var(--white) 36%,
      var(--white) 73%, #cfe2f6 84%, var(--blue) 100%);
  }

  .brand-dot {
    position: absolute;
    border-radius: 50%;
    background: var(--orange);
  }
  .card--front .brand-dot { left: 103px; top: 56px; width: 132px; height: 132px; }
  .card--back .brand-dot { left: 234px; top: 89px; width: 164px; height: 164px; }

  .wordmark {
    position: absolute;
    left: 270px; top: 62px;
    font-family: "Open Sans", sans-serif;
    font-weight: 400;
    font-size: 92px;
    letter-spacing: -2px;
    line-height: 1;
    color: var(--ink);
  }

  .person {
    position: absolute;
    right: 458px; top: 264px;
    text-align: right;
  }
  .person__name {
    font-family: "Jost", sans-serif;
    font-weight: 600;
    font-size: 22px;
    color: var(--ink);
    line-height: 28px;
  }
  .person__role {
    font-family: "Questrial", sans-serif;
    font-size: 19px;
    color: var(--ink-soft);
    line-height: 26px;
  }

  .divider {
    position: absolute;
    left: 210px; top: 245px;
    width: 3px; height: 112px;
    background: var(--orange);
  }

  .contacts {
    position: absolute;
    left: 238px; top: 240px;
    list-style: none;
  }
  .contacts li {
    display: flex;
    align-items: center;
    height: 30.5px;
    font-family: "Questrial", sans-serif;
    font-size: 18px;
    color: var(--ink);
  }
  .contacts svg { width: 18px; height: 18px; margin-right: 11px; flex: none; }

  .tagline {
    position: absolute;
    left: 0; right: 0; top: 290px;
    text-align: center;
    font-family: "Jost", sans-serif;
    font-weight: 600;
    font-size: 37px;
    color: var(--ink);
  }
</style>
</head>
<body>
<main class="canvas">

  <section class="card card--front" aria-label="Business card front">
    <div class="brand-dot" aria-hidden="true"></div>
    <div class="wordmark">velmora</div>

    <div class="person">
      <p class="person__name">Your Name</p>
      <p class="person__role">Position</p>
    </div>

    <div class="divider" aria-hidden="true"></div>

    <ul class="contacts">
      <li>
        <svg viewBox="0 0 18 18" aria-hidden="true"><path d="M4 2 L7 2 L8 6 L6 7.5 Q7.5 11 10.5 12 L12 10 L16 11 L16 14 Q15 16 12.5 15.5 Q4 13 2.5 5 Q2.5 2.5 4 2 Z" fill="none" stroke="#f07820" stroke-width="1.6" stroke-linejoin="round"/></svg>
        123-456-7890
      </li>
      <li>
        <svg viewBox="0 0 18 18" aria-hidden="true"><rect x="4.5" y="1.5" width="9" height="15" rx="1.5" fill="none" stroke="#f07820" stroke-width="1.5"/><line x1="7.5" y1="14" x2="10.5" y2="14" stroke="#f07820" stroke-width="1.3"/></svg>
        123-456-7888
      </li>
      <li>
        <svg viewBox="0 0 18 18" aria-hidden="true"><rect x="1.5" y="4" width="15" height="10" fill="none" stroke="#f07820" stroke-width="1.4"/><path d="M1.5 4 L9 10 L16.5 4" fill="none" stroke="#f07820" stroke-width="1.4"/></svg>
        name@velmora.com.eu
      </li>
      <li>
        <svg viewBox="0 0 18 18" aria-hidden="true"><circle cx="9" cy="9" r="7.5" fill="none" stroke="#f07820" stroke-width="1.4"/><ellipse cx="9" cy="9" rx="3.2" ry="7.5" fill="none" stroke="#f07820" stroke-width="1.2"/><line x1="1.5" y1="9" x2="16.5" y2="9" stroke="#f07820" stroke-width="1.2"/><line x1="3" y1="5" x2="15" y2="5" stroke="#f07820" stroke-width="1"/><line x1="3" y1="13" x2="15" y2="13" stroke="#f07820" stroke-width="1"/></svg>
        www.velmora.com.eu
      </li>
    </ul>
  </section>

  <section class="card card--back" aria-label="Business card back">
    <div class="brand-dot" aria-hidden="true"></div>
    <p class="tagline">E-assessment made easy</p>
  </section>

</main>
</body>
</html>
```